依頼詳細
ホームページ料金の価格破壊を行いたいです。納品が1週間以内で早い!!イラストよりも写真を使ってほしいです。
記載項目
社名等も入れますが、上記の内容を考慮して作っていただけると助かります。
よろしくお願いいたします。
サイズ
A4
ページ数
片面
希望イメージ
シンプル 複雑
単色 カラフル
暗い 明るい
日常 高級
遊び心 厳粛
未来的 伝統的
女性的 男性的
希望する色
お任せいたします。
納品ファイル
• 高解像度JPG (.jpg)
• イラストレーター形式 (.ai)
〒471-0093
大阪市淀川区東川原3-4-17
ミツバ第2北梅田4階
0120-914-562
この住所を明記ください。
月々の料金なし!!ポッキリ 5万円!!
プロの作ったホームページが5万円!!みたいな
友達に作ってもらった安かろう悪かろうではなく、本当の高品質なホームページが作れる集団です。みたいなことを入れてほしい。

写真が奇麗でいいなあ!と思いました。

他にも良いデザインがたくさんありました。迷いましたが・・・・みなさんありがとうございました。

```html
<!DOCTYPE html>
<html lang="ja">
<head>
<meta charset="utf-8">
<title>ホームページ制作 5万円</title>
<link href="https://fonts.googleapis.com/css2?family=Noto+Sans+JP:wght@400;500;700;900&family=Roboto:wght@500;700;900&display=swap" rel="stylesheet">
<style>
:root{
  --blue:#1f8fd6;
  --blue-dark:#0f6fb5;
  --blue-light:#d9eefa;
  --text:#333;
  --muted:#666;
  --white:#fff;
  --bg:#fff;
}
*{margin:0;padding:0;box-sizing:border-box}
html,body{width:849px;height:1200px;overflow:hidden;background:var(--bg)}
body{font-family:"Noto Sans JP",sans-serif;color:var(--text);position:relative}
.hero{position:absolute;left:0;top:0;width:849px;height:640px}
.hero-photo{position:absolute;inset:0;background:
  radial-gradient(ellipse 320px 300px at 640px 260px,#e9d6c6 0%,#f2e7dc 45%,rgba(245,240,234,0) 75%),
  linear-gradient(180deg,#f7f4ef 0%,#efe9e1 60%,#e6ddd2 100%)}
.headline{position:absolute;left:28px;top:22px}
.headline span{display:table;background:var(--blue);color:var(--white);font-weight:700;font-size:33px;line-height:1;padding:11px 14px;margin-bottom:8px;letter-spacing:1px}
.tagline{position:absolute;left:28px;top:325px;width:340px;height:74px;background:var(--blue);color:var(--white);border-radius:37px;text-align:center;font-weight:700;line-height:1.15;padding-top:8px;white-space:nowrap}
.tagline .small{font-size:22px;display:block}
.tagline .big{font-size:26px;display:block}
.price{position:absolute;left:34px;top:405px;color:var(--blue);font-weight:900;line-height:1}
.price .num{font-family:"Roboto",sans-serif;font-size:190px;letter-spacing:-4px}
.price .unit{font-size:82px;margin-left:4px}
.price-tax{position:absolute;left:425px;top:535px;color:var(--blue);font-weight:900;font-size:40px;line-height:1;white-space:nowrap}
.price-tax .num{font-family:"Roboto",sans-serif}
.price-tax small{font-size:26px}
.features{position:absolute;left:16px;top:588px;width:817px;display:flex;gap:6px;list-style:none}
.features li{flex:1 1 0;min-width:0;background:var(--blue);color:var(--white);font-weight:700;font-size:15.5px;text-align:center;height:40px;line-height:40px;white-space:nowrap;overflow:hidden}
.points{position:absolute;left:20px;top:655px;width:809px;display:flex;gap:24px}
.point{flex:1;min-width:0}
.point h2{font-size:21px;font-weight:700;color:var(--blue);margin-bottom:10px;letter-spacing:.5px;white-space:nowrap}
.point p{font-size:12.5px;line-height:1.9;color:var(--text)}
.contact{position:absolute;left:0;top:930px;width:849px;height:140px;background:var(--blue-light);border-top:3px solid var(--blue)}
.contact-lead{position:absolute;left:22px;top:20px;width:136px;height:96px;background:var(--blue);color:var(--white);font-weight:700;font-size:15px;line-height:1.6;display:flex;align-items:center;justify-content:center;text-align:center;border-radius:6px;white-space:nowrap}
.tel{position:absolute;left:172px;top:16px;display:flex;align-items:center;gap:8px;color:var(--blue-dark)}
.tel .number{font-family:"Roboto",sans-serif;font-weight:900;font-size:60px;line-height:1;letter-spacing:1px;white-space:nowrap}
.tel-hours{position:absolute;left:728px;top:26px;font-size:11px;line-height:1.5;color:var(--muted);white-space:nowrap}
.web{position:absolute;left:172px;top:88px;display:flex;align-items:center;gap:8px;color:var(--blue-dark);font-family:"Roboto",sans-serif;font-weight:700;font-size:27px;white-space:nowrap}
.footer{position:absolute;left:0;top:1082px;width:849px;height:118px}
.brand{position:absolute;left:34px;top:28px;display:flex;align-items:center;gap:12px}
.brand .mark{width:34px;height:34px;border-radius:50%;background:var(--blue)}
.brand .name{font-size:36px;font-weight:700;color:var(--blue-dark);letter-spacing:.5px;white-space:nowrap}
.company{position:absolute;left:300px;top:18px;font-size:12.5px;line-height:1.6;color:var(--text);font-style:normal;white-space:nowrap}
.company strong{font-size:16px;display:block;margin-bottom:2px}
</style>
</head>
<body>
<section class="hero">
  <div class="hero-photo" role="img" aria-label="明るい部屋でノートパソコンに向かい微笑む女性の写真"></div>
  <h1 class="headline">
    <span>お客さまが</span>
    <span>見やすく使いやすい</span>
    <span>ホームページを</span>
    <span>制作いたします。</span>
  </h1>
  <div class="tagline"><span class="small">そして</span><span class="big">高品質なのにこの価格!</span></div>
  <p class="price"><span class="num">5</span><span class="unit">万円</span></p>
  <p class="price-tax"><span class="num">52,500</span>円<small>(税込)</small></p>
  <ul class="features">
    <li>独自SEO対策</li>
    <li>1週間以内納品</li>
    <li>月々の料金なし</li>
    <li>ドメイン取得料込み</li>
    <li>サーバー設定込み</li>
  </ul>
</section>

<section class="points">
  <div class="point">
    <h2>プロが制作する高品質なデザイン。</h2>
    <p>ホームページを持っていないかたは、<br>その時点で損をしているかもしれない時代です。<br>でも、知り合いに頼んだ安かろう悪かろうではなく、<br>ホームページが大きな役割を持っている現在では<br>高品質なホームページを制作することが重要です。<br>私たちはプロの技術で本当に伝わるデザインをお届けします。</p>
  </div>
  <div class="point">
    <h2>集客に特化した独自SEO対策。</h2>
    <p>さまざまなニーズに対応した独自SEO対策は、<br>いかに集客できるかにこだわりました。<br>公開後も一定期間、順位の変化を確認しながら、<br>インターネット社会で埋もれないための工夫を重ねます。<br>見られるホームページで、多くの人に届けます。<br>月々の料金なしで安心してご利用いただけます。</p>
  </div>
</section>

<section class="contact">
  <div class="contact-lead">何でもお気軽に<br>ご相談ください。</div>
  <div class="tel">
    <svg width="52" height="52" viewBox="0 0 52 52" aria-hidden="true"><rect width="52" height="52" rx="8" fill="#0f6fb5"/><path d="M17 12c2 0 3 4 4 7 0 2-2 3-2 4 1 4 6 9 10 10 1 0 2-2 4-2 3 1 7 2 7 4 0 3-3 6-6 6-12 0-23-11-23-23 0-3 3-6 6-6z" fill="#fff"/></svg>
    <span class="number">0120-914-562</span>
  </div>
  <p class="tel-hours">受付時間<br>AM9:00〜PM6:00<br>土日祝休み</p>
  <div class="web">
    <svg width="30" height="30" viewBox="0 0 30 30" aria-hidden="true"><circle cx="15" cy="15" r="13" fill="none" stroke="#0f6fb5" stroke-width="2.5"/><ellipse cx="15" cy="15" rx="5.5" ry="13" fill="none" stroke="#0f6fb5" stroke-width="2"/><line x1="2" y1="15" x2="28" y2="15" stroke="#0f6fb5" stroke-width="2"/></svg>
    <span>http://www.soraworks.co.jp/</span>
  </div>
</section>

<footer class="footer">
  <div class="brand"><span class="mark"></span><span class="name">sora works</span></div>
  <address class="company">
    <strong>株式会社 ソラワークス</strong>
    〒471-0093 大阪市淀川区東川原3-4-17 ミツバ第2北梅田4階<br>
    TEL 06-4862-3157 FAX 06-4862-3158
  </address>
</footer>
</body>
</html>
```